■依頼の目的/概要
電子書籍の表紙デザインをお願いします。

経営者のための「黄金オフィス気学」
〜歴史に名を遺す名将や成功者はみんなやっていた〜

著者
経営者専属:開運鑑定士 夕凪みのり

★読者限定プレゼント→今すぐあなたや社員の吉方位が分かる「本命掛早見表と八宅盤」

■本の内容
経営者向けの経営サポート本として「ビジネス風水」を具体的にご紹介しています。
「まえがき、目次、本文、後書き」原稿をファイル添付していますので、まえがきや目次等見ていただき、内容の雰囲気をご確認いただけると嬉しいです。

筆者(私)はタロット歴20年の電話占い師(夕凪みのり)です。本書の著者の肩書きは↑にも書いておりますように「経営者専属:開運鑑定士 夕凪みのり」でお願い致します。

■デザイン要望
経営者に魅力を感じていただきやすくパッと目を引き、どのような本なのかが一目で分かりやすいデザインが望ましいです。基本全部おまかせです。是非デザイナーさんの魅力と才能を発揮していただけたらと思います。

その他何かご不明な点がございましたら、お気軽にご質問下さい。
よろしくお願いいたします。
【画像サイズ】※RLQより抜粋(電子書籍はLumoraです)
表紙ファイルの理想的な寸法は、2,560✖️1,600ピクセルです。
注:画像の寸法は、1,000✖️625ピクセル以上であることが必要です。
画像の最大の寸法は、10,000✖️10,000ピクセルです。

Zentaro(Lumora)に表示された際はかなり小さくなる事を踏まえ、他の経営者向けの本と並んだ時、目が止まりやすい一冊になるか?という点を意識し、選ばさせて頂きました。

表紙デザインの色や見た目のインパクトと文字の分かりやすさ、サブタイトルまでしっかりアピールされている所が気に入りました。

クラフターの皆様、この度はコンペにご参加いただきまして誠にありがとうございました。
本当に素晴らしいデザインばかりで、正直選考はとても難航いたしました。

今回は沢山のご提案の中から1つを選ぶことがとても難しかった為「他の経営者向けの本と並んだ時、目が止まりやすい一冊になるか?内容が分かりやすいか?」を軸に、著者仲間30名にアンケートを実施し当選作品を決定させて頂きました。

改めまして、皆様の才能を発揮して頂き素晴らしい作品をご提案頂きました事、心より感謝申し上げます。誠にありがとうございました。

```html
<!DOCTYPE html>
<html lang="ja">
<head>
<meta charset="utf-8">
<title>経営者のための「黄金オフィス気学」</title>
<link rel="stylesheet" href="https://fonts.googleapis.com/css2?family=Noto+Serif+JP:wght@500;700;900&family=Noto+Sans+JP:wght@700;900&family=Yuji+Syuku&display=swap">
<style>
  :root {
    --ink: #0d0606;
    --photo-dark: #1a0a08;
    --photo-red: #6e1710;
    --gold: #f5e21a;
    --white: #ffffff;
    --pink: #e66a9a;
    --band-top: #8e0f13;
    --band-bottom: #5c0709;
    --circle: #ffffff;
  }
  * { margin: 0; padding: 0; box-sizing: border-box; }
  html, body { width: 750px; height: 1200px; overflow: hidden; background: var(--ink); }
  .cover { position: relative; width: 750px; height: 1200px; overflow: hidden; font-family: "Noto Serif JP", serif; color: var(--white); }

  .cover-photo {
    position: absolute; left: 0; top: 0; width: 750px; height: 730px;
    background:
      radial-gradient(ellipse 55% 40% at 62% 52%, rgba(150,40,25,0.75), transparent 70%),
      linear-gradient(160deg, var(--photo-dark) 0%, var(--photo-red) 55%, #2a0a07 100%);
  }

  .series-tag {
    position: absolute; left: 240px; top: 12px; width: 50px; height: 178px;
    border: 2px solid var(--white); border-radius: 25px;
    display: flex; justify-content: center; padding-top: 12px;
  }
  .series-tag-text {
    writing-mode: vertical-rl; white-space: nowrap;
    font-family: "Noto Serif JP", serif; font-weight: 700; font-size: 26px; line-height: 1; letter-spacing: 1px;
  }
  .series-tag-text small { font-size: 16px; }

  .title { position: absolute; left: 0; top: 0; width: 750px; }
  .title-bracket-open { position: absolute; left: 205px; top: 195px; font-size: 150px; font-weight: 900; line-height: 1; }
  .title-main {
    position: absolute; left: 290px; top: 190px; font-family: "Noto Serif JP", serif;
    font-weight: 900; font-size: 200px; line-height: 1; color: var(--gold); letter-spacing: -4px;
    text-shadow: 0 4px 14px rgba(0,0,0,0.6);
  }
  .title-sub {
    position: absolute; left: 55px; top: 410px; white-space: nowrap; line-height: 1;
    text-shadow: 0 3px 10px rgba(0,0,0,0.6);
  }
  .title-sub .katakana { font-family: "Noto Sans JP", sans-serif; font-weight: 900; font-size: 104px; letter-spacing: -2px; }
  .title-sub .kanji { position: relative; font-family: "Noto Serif JP", serif; font-weight: 500; font-size: 104px; }
  .title-sub .kanji .dot { position: absolute; top: -24px; width: 14px; height: 14px; border-radius: 50%; background: var(--pink); }
  .title-sub .kanji .dot.one { left: 45px; }
  .title-sub .kanji .dot.two { left: 149px; }
  .title-sub .bracket-close { font-family: "Noto Serif JP", serif; font-weight: 700; font-size: 104px; }

  .author { position: absolute; left: 322px; top: 572px; }
  .author-name { font-family: "Noto Serif JP", serif; font-weight: 700; font-size: 44px; letter-spacing: 3px; text-shadow: 0 2px 8px rgba(0,0,0,0.7); }
  .author-role { margin-top: 8px; font-family: "Noto Sans JP", sans-serif; font-weight: 700; font-size: 15px; opacity: 0.9; }

  .promo-band {
    position: absolute; left: 0; top: 725px; width: 750px; height: 475px;
    background: linear-gradient(180deg, var(--band-top) 0%, var(--band-bottom) 100%);
  }
  .promo-band::before { content: ""; position: absolute; left: 0; top: 0; width: 100%; height: 6px; background: linear-gradient(180deg, rgba(0,0,0,0.45), transparent); }

  .catch-seal {
    position: absolute; left: 22px; top: 122px; width: 218px; height: 218px; border-radius: 50%;
    background: var(--circle); color: var(--ink);
    font-family: "Yuji Syuku", serif; line-height: 1;
  }
  .catch-seal span { position: absolute; font-size: 62px; }
  .catch-seal .ch-sho { left: 24px; top: 52px; }
  .catch-seal .ch-ki { left: 104px; top: 22px; }
  .catch-seal .ch-wo { left: 124px; top: 94px; font-size: 24px; }
  .catch-seal .ch-tsuka { left: 72px; top: 124px; }
  .catch-seal .ch-mu { left: 138px; top: 130px; }

  .catch-copy { position: absolute; left: 272px; top: 92px; font-family: "Noto Sans JP", sans-serif; font-weight: 900; line-height: 1.45; }
  .catch-copy .line { display: block; font-size: 50px; white-space: nowrap; }
  .catch-copy .line.indent { padding-left: 26px; }

  .reader-gift { position: absolute; left: 0; bottom: 40px; width: 750px; text-align: center; font-family: "Noto Sans JP", sans-serif; font-weight: 700; font-size: 21px; line-height: 1.7; }
</style>
</head>
<body>
<main class="cover">
  <div class="cover-photo" role="img" aria-label="赤い紙に墨の漢字が書かれた背景に、紐で結ばれた古銭が並ぶ写真"></div>

  <div class="series-tag"><span class="series-tag-text">経営者<small>の</small>ための</span></div>

  <h1 class="title">
    <span class="title-bracket-open">「</span>
    <span class="title-main">黄金</span>
    <span class="title-sub">
      <span class="katakana">オフィス</span><span class="kanji">気学<i class="dot one"></i><i class="dot two"></i></span><span class="bracket-close">」</span>
    </span>
  </h1>

  <div class="author">
    <p class="author-name">夕凪みのり</p>
    <p class="author-role">経営者専属｜開運鑑定士</p>
  </div>

  <section class="promo-band">
    <div class="catch-seal" aria-label="勝機を掴む">
      <span class="ch-sho">勝</span>
      <span class="ch-ki">機</span>
      <span class="ch-wo">を</span>
      <span class="ch-tsuka">掴</span>
      <span class="ch-mu">む</span>
    </div>
    <p class="catch-copy">
      <span class="line">歴史に名を遺す</span>
      <span class="line indent">名将や成功者は</span>
      <span class="line">みんなやっていた！</span>
    </p>
    <p class="reader-gift">読者限定プレゼント<br>今すぐあなたや社員の吉方位が分かる「本命掛早見表と八宅盤」</p>
  </section>
</main>
</body>
</html>
```